Business card design needed-Cake Decorating

I personalize designer cakes without the designer price. I was thinking about a card design that is a little funky, modern and fun. I am very open to suggestions though

Industry/Entity Type

Business

Contact Information for Business Card

Whisk & Bloom Bakehouse
Ph: Mara Pelling 0438105274
Email:mara@whiskbloombakehouse.com.au
Website:www.whiskbloombakehouse.com.au
ABN: 47 293816054

```html
<!DOCTYPE html>
<html lang="en">
<head>
<meta charset="utf-8">
<title>Whisk &amp; Bloom Bakehouse – Business Card</title>
<link href="https://fonts.googleapis.com/css2?family=Marcellus&display=swap" rel="stylesheet">
<style>
  :root {
    --paper: #ffffff;
    --ink: #111111;
    --tier-top: #9c1c3b;
    --tier-middle: #ee295a;
    --tier-bottom: #e92d8d;
  }
  html, body {
    margin: 0;
    padding: 0;
    overflow: hidden;
    background: var(--paper);
  }
  .card {
    position: relative;
    width: 1200px;
    height: 747px;
    background: var(--paper);
    overflow: hidden;
    font-family: "Marcellus", serif;
    color: var(--ink);
  }
  .cake-artwork {
    position: absolute;
    left: 590px;
    top: 45px;
    width: 500px;
    height: 565px;
    border-radius: 36px 36px 70px 70px / 30px 30px 60px 60px;
    background: linear-gradient(180deg,
      var(--tier-top) 0%,
      var(--tier-top) 30%,
      var(--tier-middle) 40%,
      var(--tier-middle) 56%,
      var(--tier-bottom) 68%,
      var(--tier-bottom) 100%);
  }
  .contact {
    position: absolute;
    margin: 0;
    white-space: nowrap;
    text-align: center;
    line-height: 1;
  }
  .contact-name {
    left: 612px;
    width: 420px;
    top: 148px;
    font-size: 42px;
  }
  .contact-phone {
    left: 612px;
    width: 420px;
    top: 196px;
    font-size: 42px;
    letter-spacing: 1px;
  }
  .contact-email {
    left: 615px;
    width: 430px;
    top: 372px;
    font-size: 26px;
    letter-spacing: -0.5px;
    transform: rotate(-4deg);
  }
  .contact-web {
    left: 600px;
    width: 480px;
    top: 525px;
    font-size: 28px;
    letter-spacing: -0.5px;
    transform: rotate(-4deg);
  }
  .brand-name {
    position: absolute;
    left: 10px;
    top: 615px;
    margin: 0;
    font-size: 48px;
    font-weight: 400;
    line-height: 1;
    white-space: nowrap;
    color: var(--ink);
  }
</style>
</head>
<body>
  <main class="card">
    <div class="cake-artwork" role="img" aria-label="Playful hand-drawn three-tier cake in maroon, raspberry and hot pink with bold outlines, carrying the contact details"></div>

    <p class="contact contact-name">Mara Pelling</p>
    <p class="contact contact-phone">043-810-5274</p>
    <p class="contact contact-email">mara@whiskbloombakehouse.com.au</p>
    <p class="contact contact-web">www.whiskbloombakehouse.com.au</p>

    <h1 class="brand-name">Whisk &amp; Bloom Bakehouse</h1>
  </main>
</body>
</html>
```